Veteran Owned General Contractor needs Bold New Business Cards

We are a service disabled veteran owned small business. We're a general contractor that specializes in excavation, underground utilities, site work, land clearing and demolition. We would like a fresh, simple, bold, new look for our business cards. We're open to ideas! We'd like to incorporate the following information on the card:

Company Name & Logo, Name of Person, Job Title, Office Phone, Fax, Cell Phone, Email Address, Website, SDVOSB

Our logo is included. We look forward to your thoughts.

Thank you!
Updates

Reason: Hello Due to the overwhelming response to this project, we are extending the deadline one time to allow for improved communication and feedback with the top candidates. We would like to thank everyone for their hard work and exceptional creativity! Thank you

Industry/Entity Type

Business

Contact Information for Business Card

Font styles to use
Sans Serif

Requirements
Nice to have
• As we are a veteran owned company, it would be nice to incorporate an American flag into the design. Maybe on the back?

```html
<!DOCTYPE html>
<html lang="en">
<head>
<meta charset="utf-8">
<title>Ridgeline Business Cards</title>
<link href="https://fonts.googleapis.com/css2?family=Roboto:wght@400;500;900&display=swap" rel="stylesheet">
<style>
  :root {
    --bg: #d9d6d2;
    --card: #121212;
    --green: #6cc04a;
    --white: #f2f2f2;
    --grey: #8a8a8a;
    --flag-red: #b22234;
    --flag-blue: #3c3b6e;
  }
  * { margin: 0; padding: 0; box-sizing: border-box; }
  html, body { width: 1200px; height: 864px; overflow: hidden; }
  body {
    background: var(--bg);
    font-family: "Roboto", sans-serif;
    position: relative;
  }
  .card {
    position: absolute;
    top: 277px;
    width: 540px;
    height: 309px;
    background: var(--card);
    border-radius: 3px;
    box-shadow: 0 8px 24px rgba(0,0,0,.35);
    overflow: hidden;
  }
  .card-back { left: 40px; }
  .card-front { left: 620px; }

  .flag-art {
    position: absolute;
    left: 0; top: 14px;
    width: 190px; height: 150px;
    background: linear-gradient(135deg, var(--flag-blue) 0 30%, var(--flag-red) 30% 60%, #e8e8e8 60% 75%, #9a9a9a 75%);
    opacity: .9;
  }

  .brand {
    position: absolute;
    display: flex;
    align-items: center;
    gap: 10px;
  }
  .brand-mark {
    width: 30px; height: 30px;
    background: var(--grey);
  }
  .brand-name {
    font-weight: 900;
    color: var(--green);
    letter-spacing: 1px;
  }
  .card-back .brand { right: 60px; top: 175px; }
  .card-back .brand-name { font-size: 38px; }
  .back-web {
    position: absolute;
    right: 60px; top: 228px;
    color: var(--grey);
    font-size: 12px;
    letter-spacing: 5px;
  }

  .card-front .brand { right: 30px; top: 38px; }
  .card-front .brand-name { font-size: 32px; }
  .person {
    position: absolute;
    left: 30px; top: 118px;
  }
  .person-name { color: var(--green); font-size: 18px; font-weight: 500; }
  .person-title { color: var(--white); font-size: 13px; margin-top: 3px; }
  .divider {
    position: absolute;
    left: 30px; right: 30px; top: 170px;
    border-top: 1.5px solid var(--white);
  }
  .phones {
    position: absolute;
    left: 30px; top: 182px;
    list-style: none;
  }
  .phones li, .online li {
    display: flex; align-items: center; gap: 8px;
    color: var(--white); font-size: 13px; line-height: 22px;
  }
  .phones svg, .online svg { width: 12px; height: 12px; fill: var(--green); }
  .online {
    position: absolute;
    right: 30px; bottom: 24px;
    list-style: none;
  }
  .online li { justify-content: flex-end; }
</style>
</head>
<body>
  <section class="card card-back">
    <div class="flag-art" role="img" aria-label="Waving American flag on a flagpole"></div>
    <div class="brand">
      <span class="brand-mark"></span>
      <span class="brand-name">RIDGELINE</span>
    </div>
    <p class="back-web">www.ridgelineworks.com</p>
  </section>

  <section class="card card-front">
    <div class="brand">
      <span class="brand-mark"></span>
      <span class="brand-name">RIDGELINE</span>
    </div>
    <div class="person">
      <p class="person-name">Sam Carter</p>
      <p class="person-title">President</p>
    </div>
    <div class="divider"></div>
    <ul class="phones">
      <li><svg viewBox="0 0 12 12"><path d="M2 1h3l1 3-2 1a6 6 0 0 0 3 3l1-2 3 1v3c-6 1-10-3-9-9z"/></svg>555 201 3344</li>
      <li><svg viewBox="0 0 12 12"><path d="M3 0h6v12H3zM4 1v9h4V1z"/></svg>555 201 3345</li>
      <li><svg viewBox="0 0 12 12"><path d="M1 4h10v7H1zM3 0h6v3H3z"/></svg>555 201 3346</li>
    </ul>
    <ul class="online">
      <li>sam@ridgelineworks.com<svg viewBox="0 0 12 12"><path d="M0 2h12v8H0zM1 3l5 4 5-4z"/></svg></li>
      <li>www.ridgelineworks.com<svg viewBox="0 0 12 12"><path d="M6 0a4 4 0 0 1 4 4c0 3-4 8-4 8S2 7 2 4a4 4 0 0 1 4-4z"/></svg></li>
    </ul>
  </section>
</body>
</html>
```